BrookVale Collision Repair Web Site

Create a web site that will inform my potential customers about the services I provide. We are a Automotive Collision repair business that uses the latest state of the art equipment, computerized paint matching highly trained technicians, have over 30 years experience. We work with all all insurance programs. Our Moto is "Fixed Right, The First Time, Every Time". BrookVale, The trusted pick in collision repair.

Target Market(s)

People that have been in a auto collision, needs windshield replaced, people that drive 10 year or newer cars

Industry/Entity Type

Automotive

Coding

Coded - Design and coding required

Number of Pages Required

4 page

Font styles to use
Sans Serif

Requirements
Must have
• Logo, Place for Phone number, I need to be able to put the code in so I can use a tracking phone number
• site needs to be mobile ready or adaptive
• May want to have a photo of a high end car
• here is a web site for example with the pages that I want
• https://www.pondlyautobody.example/online-repair-estimate,
• https://www.pondlyautobody.example/schedule-appointment
• https://www.pondlyautobody.example/collision-repair/auto-body-repair
• https://www.pondlyautobody.example/contact
Nice to have
• Be great if the Car in the log could have the front damaged then have it fix in a animation. Not sure if could be done here

```html
<!DOCTYPE html>
<html lang="en">
<head>
<meta charset="utf-8">
<title>BrookVale Collision Repair</title>
<link href="https://fonts.googleapis.com/css2?family=Arimo:wght@400;700&family=Tinos:wght@400;700&display=swap" rel="stylesheet">
<style>
:root{
  --blue:#1a4a94;
  --navy:#0f3272;
  --ink:#555;
  --red:#e03a3a;
  --lime:#b6f03c;
  --page:#f5f5f5;
  --footer:#6b6a66;
  --field:#f4f6fa;
}
*{box-sizing:border-box;margin:0;padding:0}
html,body{width:720px;height:1200px;overflow:hidden;background:var(--page)}
body{position:relative;font-family:"Arimo",Arial,sans-serif;color:var(--ink)}
.abs{position:absolute}

.brand{left:87px;top:28px;display:flex;align-items:center;gap:8px;font-weight:700;font-size:20px;color:var(--blue)}
.brand-dot{width:14px;height:14px;border-radius:50%;background:var(--blue)}
.brand small{display:block;font-size:10px;letter-spacing:1px}
.phone{right:85px;top:21px;display:flex;align-items:center;gap:6px;font-size:15px;color:var(--blue)}
.phone-icon{width:17px;height:17px;background:#5a9a2a;border-radius:3px;display:flex;align-items:center;justify-content:center}
.social-top{right:85px;top:47px;display:flex;gap:3px}
.social-top span{width:18px;height:18px;border-radius:3px}

.nav{left:0;top:82px;width:720px;height:32px;background:var(--blue);display:flex;justify-content:center;align-items:center;font-size:13px;color:#fff}
.nav a{color:#fff;text-decoration:none}
.nav a.current{color:var(--lime)}
.nav .sep{margin:0 20px}

.hero{left:0;top:114px;width:720px;height:182px;background:linear-gradient(180deg,#b9c0c5 0%,#d3d7da 45%,#a9b0b5 75%,#c4c8cb 100%)}
.hero-title{left:84px;top:174px;font-family:"Tinos",serif;font-size:27px;color:#fff;text-shadow:0 1px 3px rgba(0,0,0,.6)}
.hero-line{font-family:"Tinos",serif;color:#fff;text-shadow:0 1px 3px rgba(0,0,0,.7);font-size:14px}
.dots{left:132px;top:271px;display:flex;gap:4px}
.dots span{width:11px;height:11px;border-radius:50%;background:#ddd}
.dots span:first-child{background:#aab}

.welcome{left:0;top:318px;width:720px;text-align:center;font-size:16px;font-weight:700;color:var(--blue)}
.intro{left:86px;top:363px;width:538px;text-align:center;font-size:10.8px;line-height:13.4px}

.band{left:0;top:502px;width:720px;height:215px;background:var(--blue)}
.need{left:87px;top:528px;font-size:15px;color:#fff;font-weight:400}
.appt{left:87px;top:557px;font-family:"Tinos",serif;font-weight:700;font-size:13px;color:var(--red)}
.walk{left:87px;top:587px;width:205px;font-size:9.8px;line-height:12px;color:#fff}

.estimate{left:344px;top:470px;width:292px;height:271px;background:var(--navy);border-radius:14px}
.estimate h2{position:absolute;top:13px;width:100%;text-align:center;font-weight:400;font-size:14px;color:#fff}
.field{position:absolute;height:22px;background:var(--field);border:1px solid #c8d0dc;border-radius:3px;font-size:10px;color:#666;padding:4px 7px}
.field.left{left:17px;width:123px}
.field.right{left:153px;width:124px}
.field.wide{left:17px;top:142px;width:260px;height:38px}
.upload{position:absolute;left:11px;top:194px;display:flex;align-items:center;gap:4px;font-size:7.4px;color:#fff;white-space:nowrap}
.upload .btn{background:#5aa82a;padding:5px 6px;font-weight:700}
.claim{position:absolute;left:12px;top:219px;font-size:7.4px;color:#fff;display:flex;gap:8px;align-items:center;white-space:nowrap}
.claim i{display:inline-block;width:7px;height:7px;border-radius:50%;background:#fff;margin-right:4px;vertical-align:-1px}
.submit{position:absolute;left:106px;top:240px;width:87px;height:21px;border-radius:3px;overflow:hidden;background:linear-gradient(#2e7ad8,#0d4aa0);display:flex;font-size:8.5px;font-weight:700;color:#fff}
.submit span{flex:1;display:flex;align-items:center;justify-content:center}
.submit b{width:20px;background:#16386d;display:flex;align-items:center;justify-content:center}

.why{left:87px;top:777px;font-size:13px;font-weight:700;color:var(--blue)}
.reasons{left:87px;top:810px;width:545px;font-size:10px;line-height:12px;list-style:none}
.reasons li{position:relative;padding-left:14px;margin-bottom:5px}
.reasons li::before{content:"";position:absolute;left:3px;top:4px;width:4px;height:4px;border-radius:50%;background:#777}

.t-head{left:0;top:947px;width:720px;text-align:center;font-size:19px;color:var(--blue);font-weight:400}
.quote{left:145px;top:979px;width:430px;text-align:center;font-size:10px;line-height:12.5px}
.qmark{font-family:"Tinos",serif;font-size:34px;color:#bbb}
.avatar{left:251px;top:1034px;width:48px;height:48px;border-radius:50%;background:var(--blue)}
.arrow{font-size:24px;color:#777}
.who{left:321px;top:1047px;font-size:10px;line-height:16px}
.who b{font-weight:400;color:var(--red)}

.footer{left:0;top:1115px;width:720px;height:85px;background:var(--footer)}
.copy{left:87px;top:1149px;font-size:15px;color:#fff}
.social-foot{left:430px;top:1141px;display:flex;gap:8px}
.social-foot span{width:35px;height:35px;border-radius:50%;background:#4a4a48;border:2px solid #8a8a86}
</style>
</head>
<body>

<header>
  <div class="abs brand"><span class="brand-dot"></span><div>BrookVale<small>COLLISION REPAIR</small></div></div>
  <div class="abs phone"><span class="phone-icon"><svg width="11" height="11" viewBox="0 0 24 24"><path fill="#fff" d="M6.6 10.8a15 15 0 006.6 6.6l2.2-2.2c.3-.3.7-.4 1-.2 1.1.4 2.3.6 3.6.6.6 0 1 .4 1 1V20c0 .6-.4 1-1 1A17 17 0 013 4c0-.6.4-1 1-1h3.5c.6 0 1 .4 1 1 0 1.3.2 2.5.6 3.6.1.3 0 .7-.2 1z"/></svg></span>1-111-1BROOKVALE</div>
  <div class="abs social-top"><span style="background:#3b5a9a"></span><span style="background:#29a9e1"></span><span style="background:#cc2127"></span><span style="background:#f58220"></span></div>
</header>

<nav class="abs nav">
  <a class="current" href="#">Home</a><span class="sep">|</span>
  <a href="#">About Us</a><span class="sep">|</span>
  <a href="#">Services</a><span class="sep">|</span>
  <a href="#">FAQ</a><span class="sep">|</span>
  <a href="#">Testimonials</a><span class="sep">|</span>
  <a href="#">Contact</a>
</nav>

<section>
  <div class="abs hero" role="img" aria-label="Photo of a red sports car parked on a waterfront with a bridge and city skyline behind"></div>
  <div class="abs hero-title">BrookVale</div>
  <div class="abs hero-line" style="left:30px;top:207px">The Intelligent choice in Collision Repair</div>
  <div class="abs hero-line" style="left:47px;top:232px">Fixed Right, The First Time, Every Time</div>
  <div class="abs dots"><span></span><span></span><span></span></div>
</section>

<section>
  <h1 class="abs welcome">Welcome to BrookVale Collision Repair</h1>
  <p class="abs intro">For over 30 years' vehicle owners and fleet managers have trusted our staff for all their collision repairs. Our Nationwide, Lifetime Guarantee and excellent customer service are just a few of the reasons you want to choose BrookVale. We use the latest computerized frame alignment and paint matching technology. Our professional staff of certified technicians take pride in the work they do and strive to deliver the best possible service. BrookVale “The trusted pick in Collision Repair”</p>
</section>

<section>
  <div class="abs band"></div>
  <h2 class="abs need">NEED AN ESTIMATE?</h2>
  <div class="abs appt">Schedule an appointment</div>
  <p class="abs walk">Walk in estimates are welcome but we prefer to have you call us and schedule your appointment to have your estimate written. This will make sure you don't have to wait any longer than necessary and it will give us proper time to thoroughly inspect your vehicle.</p>

  <form class="abs estimate">
    <h2>Online Estimate</h2>
    <div class="field left" style="top:46px">Service Locaion:</div>
    <div class="field right" style="top:46px">Year:*</div>
    <div class="field left" style="top:78px">Make:*</div>
    <div class="field right" style="top:78px">Model:*</div>
    <div class="field left" style="top:110px">Body Style:*</div>
    <div class="field right" style="top:110px">VIN*</div>
    <div class="field wide">Description of Damage:*</div>
    <div class="upload">Add images (optional) <span class="btn">&#8595; Add files</span> .gif .jpg .png &amp; .bmp - Max 6</div>
    <div class="claim">Will an insurance claim be submied for damages? <span><i></i>Yes</span><span><i></i>No</span></div>
    <div class="submit"><span>SUBMIT</span><b><svg width="12" height="10" viewBox="0 0 12 10"><path d="M1 5l3 3 7-7" stroke="#fff" stroke-width="2" fill="none"/></svg></b></div>
  </form>
</section>

<section>
  <h2 class="abs why">Why is BrookVale the Intelligent Choice in Collision Repair?</h2>
  <ul class="abs reasons">
    <li>We ensure that latest OEM approved procedures are followed during each phase of the repair of your vehicle.</li>
    <li>We have the latest in computerized frame equipment.</li>
    <li>Our technicians are certified in structural repairs ensuring that your vehicle will be as safe for your family as it was the day it left the factory.</li>
    <li>Our refinish equipment and trained painters will make sure your finish is back to factory finish maybe even better.</li>
    <li>Each repair including paint and collision repair comes with a limited lifetime<br>warranty as long as you own the vehicle.</li>
  </ul>
</section>

<section>
  <h2 class="abs t-head">Testimonials</h2>
  <span class="abs qmark" style="left:108px;top:965px">&#8220;</span>
  <p class="abs quote">Lorem ipsum dolor sit amet, consectetur adipiscing elit, sed do eiusmod tempor Ut enim ad minim veniam, quis nostrud exercitation ullamco laboris nisi ut aliquip ex ea commodo consequat.</p>
  <span class="abs qmark" style="left:585px;top:975px">&#8221;</span>
  <span class="abs arrow" style="left:214px;top:1042px">&lt;</span>
  <div class="abs avatar" role="img" aria-label="Customer icon"></div>
  <div class="abs who"><b>By Dana Whitfield</b><br>Lorem ipsum dolor sit amet</div>
  <span class="abs arrow" style="left:460px;top:1042px">&gt;</span>
</section>

<footer>
  <div class="abs footer"></div>
  <div class="abs copy">Copyright @ BrookVale 2016</div>
  <div class="abs social-foot"><span></span><span></span><span></span><span></span><span></span></div>
</footer>

</body>
</html>
```